Looking for something outstanding

2 side business card, one side just the logo preferably the metallic 3D color or my original logo for uv printing. Be creative

Colors

Designer to choose colors to be used in the design.

Requirements
Must have
• Here my info for the business cards
• Owen Hardy
• President
• (555) 302-8816
• Owen@cobaltbuildgroup.com
• Office@cobaltbuildgroup.com
• www.cobaltbuildgroup.com
• FB @cobaltbuildgroup
• Dallas-Fort Worth

```html
<!DOCTYPE html>
<html lang="en">
<head>
<meta charset="utf-8">
<title>Cobalt Build Group — Business Card</title>
<link href="https://fonts.googleapis.com/css2?family=Montserrat:wght@400;500;600&display=swap" rel="stylesheet">
<style>
  :root {
    --backdrop: #a8a8a8;
    --card: #171717;
    --card-edge: #ff1a1a;
    --ink-light: #e6e6e6;
    --ink-soft: #cfcfcf;
    --silver: #c9c9cc;
    --gloss: #2b2b2d;
  }
  * { margin: 0; padding: 0; box-sizing: border-box; }
  html, body {
    width: 1200px; height: 857px; overflow: hidden;
    background: var(--backdrop);
    font-family: "Montserrat", sans-serif;
  }
  .stage {
    width: 1200px; height: 857px;
    display: flex; align-items: center; justify-content: center; gap: 44px;
  }
  .card {
    width: 522px; height: 298px;
    background: var(--card);
    border-bottom: 3px solid var(--card-edge);
    border-right: 2px solid var(--card-edge);
    box-shadow: 0 14px 26px rgba(0,0,0,0.28);
    position: relative;
  }
  .card--info { display: flex; align-items: center; }
  .brand { display: flex; align-items: center; gap: 12px; }
  .brand__mark { width: 16px; height: 16px; background: currentColor; flex: none; }
  .brand__name {
    font-weight: 500; letter-spacing: 0.14em; text-transform: uppercase; line-height: 1.25;
  }
  .card--info .brand { color: var(--silver); width: 262px; padding-left: 46px; }
  .card--info .brand__name { font-size: 17px; }
  .divider { width: 1px; height: 190px; background: var(--ink-soft); opacity: 0.8; }
  .contact { padding-left: 26px; color: var(--ink-light); }
  .contact__name {
    font-size: 15px; font-weight: 600; letter-spacing: 0.03em; text-transform: uppercase;
  }
  .contact__role { font-size: 10.5px; margin-top: 2px; color: var(--ink-soft); }
  .contact__lines { list-style: none; margin-top: 14px; font-size: 10.5px; color: var(--ink-soft); }
  .contact__lines li { display: flex; align-items: center; gap: 8px; line-height: 1.65; white-space: nowrap; }
  .contact__lines svg { width: 10px; height: 10px; flex: none; }
  .card--logo { display: flex; align-items: center; justify-content: center; }
  .card--logo .brand { color: var(--gloss); gap: 18px; }
  .card--logo .brand__mark { width: 30px; height: 30px; }
  .card--logo .brand__name { font-size: 30px; }
</style>
</head>
<body>
<main class="stage">
  <section class="card card--info" aria-label="Business card, contact side">
    <div class="brand">
      <span class="brand__mark"></span>
      <span class="brand__name">Cobalt<br>Build Group</span>
    </div>
    <div class="divider"></div>
    <div class="contact">
      <p class="contact__name">Owen Hardy</p>
      <p class="contact__role">President</p>
      <ul class="contact__lines">
        <li>
          <svg viewBox="0 0 10 10" aria-hidden="true"><rect x="2" y="0.5" width="6" height="9" rx="1" fill="none" stroke="currentColor"/></svg>
          (555) 302-8816
        </li>
        <li>
          <svg viewBox="0 0 10 10" aria-hidden="true"><rect x="0.5" y="2" width="9" height="6" fill="none" stroke="currentColor"/><path d="M0.5 2 L5 5.5 L9.5 2" fill="none" stroke="currentColor"/></svg>
          Owen@cobaltbuildgroup.com
        </li>
        <li>
          <svg viewBox="0 0 10 10" aria-hidden="true"><rect x="0.5" y="2" width="9" height="6" fill="none" stroke="currentColor"/><path d="M0.5 2 L5 5.5 L9.5 2" fill="none" stroke="currentColor"/></svg>
          Office@cobaltbuildgroup.com
        </li>
        <li>
          <svg viewBox="0 0 10 10" aria-hidden="true"><circle cx="5" cy="5" r="4.3" fill="none" stroke="currentColor"/><path d="M0.7 5 H9.3 M5 0.7 C2.5 3 2.5 7 5 9.3 M5 0.7 C7.5 3 7.5 7 5 9.3" fill="none" stroke="currentColor" stroke-width="0.7"/></svg>
          www.cobaltbuildgroup.com
        </li>
        <li>
          <svg viewBox="0 0 10 10" aria-hidden="true"><circle cx="5" cy="5" r="4.3" fill="none" stroke="currentColor"/></svg>
          FB @cobaltbuildgroup
        </li>
        <li>
          <svg viewBox="0 0 10 10" aria-hidden="true"><path d="M5 9.5 C2.5 6.5 1.5 5 1.5 3.7 A3.5 3.5 0 0 1 8.5 3.7 C8.5 5 7.5 6.5 5 9.5 Z" fill="none" stroke="currentColor"/><circle cx="5" cy="3.8" r="1.2" fill="currentColor"/></svg>
          Dallas-Fort Worth
        </li>
      </ul>
    </div>
  </section>

  <section class="card card--logo" aria-label="Business card, logo side">
    <div class="brand">
      <span class="brand__mark"></span>
      <span class="brand__name">Cobalt Build Group</span>
    </div>
  </section>
</main>
</body>
</html>
```